Photo Storage Service - Web Application

This is web design for a simple photo storage service.
There is a web page and on the left side is a list of folders and on the right side there are photo thumbnails. By pressing a photo thumbnail, they will see the full size (it's just a link to a different page).
This project is limited only to ONE page, which is the page with the folders list and the thumbnails. However it contains some features that I will try to list here:
- Name of the service: Teso Vault
- Location of account: http://username.tesovault.example
- Folder list: Show all folders belonging to the user. Because you have to be able to drag photos to a folder, they have to be visible and cannot be hidden behind a menu item etc.
- Thumbnails with photos (in the future also videos)
- Adjusted view with smaller thumbnails and less space for folder list (so it is possible to view a larger quantity of thumbnails)- Select multiple thumbnails with rectangle- Show that a thumbnail is selected (maybe bold border?)
- Simple mobile view, but no emphasis on the mobile view in this design project.
- Drag one or more selected photos to a folder
- Delete one or more selected photos
- Drag a folder to another folder
- Rename folder
- Delete folder
- Create folder
- Show progress when deleting/moving (because it calls for every photo, so if there are 100 photos, it will delete 1 by 1 and it will take about 10 seconds - you could show progress bar or equivalent)
Background information: This is for a photo storage service NOT intended for sharing photos, but intended to indefinitely store photos and for yourself to browse your own photos.
It is a design requirement that it loads extremely fast. So we need to limit as much as possible extra graphics that cannot be done by CSS and other external libraries.
(I know this is ONLY design and nothing to do with CSS or libraries, but I can assess from the design if it might be heavy to load when implemented)
I have attached a crude screenshot of the current design, just for your understanding. It should not match this design and you are not in any way supposed to FIT your design into this same style or structure.
Target Market(s)
Consumers
Number of Pages Required
1 page

```html
<!DOCTYPE html>
<html lang="en">
<head>
<meta charset="utf-8">
<title>Teso Vault – Alicante 2017</title>
<link href="https://fonts.googleapis.com/css2?family=Mulish:wght@300;400;600;700;800&display=swap" rel="stylesheet">
<style>
:root{
  --teal:#2b8d91;
  --teal-dark:#22777a;
  --navy:#1f3553;
  --ink:#2c3440;
  --muted:#6b7480;
  --line:#e4e8ec;
  --side:#f4f6f9;
  --band:#9c9c9c;
  --white:#ffffff;
}
*{box-sizing:border-box;margin:0;padding:0}
html,body{width:870px;height:1200px;overflow:hidden;background:var(--white)}
body{font-family:"Mulish",sans-serif;color:var(--ink);position:relative}
.screen{position:absolute;left:0;width:870px;overflow:hidden;background:var(--white)}
.screen-full{top:0;height:878px}
.screen-compact{top:910px;height:290px}
.separator-band{position:absolute;left:0;top:878px;width:870px;height:32px;background:var(--band)}

.sidebar{position:absolute;left:0;top:0;width:178px;height:100%;background:var(--side)}
.brand{position:absolute;top:17px;left:0;width:178px;text-align:center;font-size:12px;font-weight:600;color:var(--ink);letter-spacing:.2px}
.btn-create{position:absolute;left:10px;top:47px;width:158px;height:20px;border-radius:4px;background:var(--teal);color:var(--white);font-size:7px;font-weight:800;display:flex;align-items:center;justify-content:center;gap:4px;letter-spacing:.2px}
.folder-list{position:absolute;top:74px;left:0;width:178px;list-style:none}
.folder{height:21px;display:flex;align-items:center;padding-left:10px;font-size:7px;color:var(--ink);border-bottom:1px solid var(--line);position:relative}
.folder.sub{padding-left:26px}
.folder.two-line{height:31.5px;line-height:10px;padding-right:40px}
.folder.active{font-weight:800;color:var(--navy);background:var(--white)}
.folder.active::before{content:"";position:absolute;left:0;top:0;width:2px;height:100%;background:var(--navy)}
.folder.hover{font-weight:800;color:var(--navy);background:var(--white)}
.folder-actions{position:absolute;right:10px;top:6px;display:flex;gap:6px}
.cursor{position:absolute;left:76px;top:6px}

.topnav{position:absolute;top:8px;left:620px;display:flex;align-items:center;height:14px;font-size:6px;font-weight:700;color:var(--teal);letter-spacing:.2px}
.topnav span{margin-right:10px}
.dots{display:flex;gap:2px;margin-right:14px}
.dots i{width:3px;height:3px;border-radius:50%;background:var(--teal)}
.avatar{width:20px;height:20px;border-radius:50%;background:linear-gradient(135deg,#c9a48b,#6b4a3a);margin-right:4px}
.user{color:var(--ink);font-weight:400;font-size:7px;margin-right:6px}

.page-title{position:absolute;left:210px;top:42px;font-size:19px;font-weight:300;color:#3c4450;letter-spacing:.2px}
.rule{position:absolute;left:210px;top:72px;width:630px;height:1px;background:var(--line)}
.toolbar-label{position:absolute;left:210px;top:86px;font-size:7px;color:var(--ink)}
.view-toggle{position:absolute;top:84px;width:13px;height:13px;border-radius:3px;display:flex;align-items:center;justify-content:center}
.view-toggle.on{background:#e6eef3}
.btn-upload{position:absolute;left:753px;top:81px;width:64px;height:20px;border-radius:4px;background:var(--navy);color:var(--white);font-size:7px;font-weight:800;display:flex;align-items:center;justify-content:center;gap:3px}
.btn-trash{position:absolute;left:821px;top:81px;width:18px;height:20px;border-radius:3px;background:#eceff2;display:flex;align-items:center;justify-content:center}

.photo{position:absolute;width:151px;height:113px}
.photo.sm{width:74px;height:55px}
.photo.selected{outline:2px solid var(--teal);outline-offset:-2px}
.photo .tick{position:absolute;right:2px;top:2px;width:10px;height:10px;background:var(--teal);display:flex;align-items:center;justify-content:center}

.progress-card{position:absolute;top:508px;width:146px;height:161px;background:var(--white);border-radius:8px;box-shadow:0 4px 14px rgba(0,0,0,.25);text-align:center}
.progress-title{margin-top:28px;font-size:8.5px;font-weight:800;color:var(--teal)}
.ring{position:absolute;left:30px;top:45px}
.percent{position:absolute;left:0;width:146px;top:96px;font-size:11px;color:var(--ink)}
.completed{position:absolute;left:0;width:146px;top:113px;font-size:5px;color:var(--ink);letter-spacing:.2px}

.footer{position:absolute;top:856px;left:210px;width:630px;text-align:center;font-size:6px;color:var(--ink)}
</style>
</head>
<body>

<!-- Full view -->
<section class="screen screen-full">
  <aside class="sidebar">
    <div class="brand">Teso Vault</div>
    <div class="btn-create">
      <svg width="9" height="8" viewBox="0 0 9 8"><rect x="0" y="1" width="9" height="7" rx="1" fill="#fff"/><rect x="0" y="0" width="4" height="2" rx="1" fill="#fff"/><path d="M4.5 2.6v4M2.5 4.6h4" stroke="#2b8d91" stroke-width="1.2"/></svg>
      CREATE FOLDER
    </div>
    <ul class="folder-list">
      <li class="folder">Inbox</li>
      <li class="folder">80s party</li>
      <li class="folder sub">A day in Oslo</li>
      <li class="folder sub">Alicante after Chrismias</li>
      <li class="folder">A tour of Svendborg</li>
      <li class="folder active">Alicante 2017</li>
      <li class="folder">Bandarban</li>
      <li class="folder two-line">Birds lightly garnished with monkeys and waterfalls</li>
      <li class="folder hover">Brazil
        <svg class="cursor" width="10" height="12" viewBox="0 0 10 12"><path d="M3 1.2c.6 0 1 .4 1 1V6l.5-.3c.5-.1 1 .2 1.1.6l.3-.1c.5-.1 1 .2 1.1.6.5-.1 1 .2 1.1.7V9c0 1.5-1.2 2.6-2.6 2.6H4.6c-.8 0-1.5-.4-2-1L1 8.3c-.3-.4-.2-1 .2-1.2.4-.3.9-.2 1.2.1l.6.8V2.2c0-.6.4-1 1-1z" fill="#fff" stroke="#222" stroke-width=".7"/></svg>
        <span class="folder-actions">
          <svg width="8" height="8" viewBox="0 0 8 8"><path d="M1 7l.4-1.8L5.6 1l1.4 1.4-4.2 4.2z" fill="#1f3553"/></svg>
          <svg width="8" height="9" viewBox="0 0 8 9"><path d="M1 2h6M3 2V1h2v1M1.8 2.5l.5 5.5h3.4l.5-5.5" fill="none" stroke="#1f3553" stroke-width=".9"/></svg>
        </span>
      </li>
      <li class="folder two-line">Days in Denmark - Christmas and new years</li>
      <li class="folder">Mobile Uploads</li>
      <li class="folder sub">Random</li>
      <li class="folder sub">Recently uploaded form phone</li>
      <li class="folder sub">Timeline Photos</li>
      <li class="folder">Sundarban</li>
      <li class="folder">Sylhet ||</li>
      <li class="folder">Tea Garden</li>
      <li class="folder">Thailand I</li>
      <li class="folder">Thailand 2</li>
      <li class="folder">Thailand 2018</li>
      <li class="folder">USA</li>
      <li class="folder">UplodBag</li>
      <li class="folder">Vancouver</li>
      <li class="folder">thumbnails</li>
      <li class="folder">videos/thumbnails</li>
    </ul>
  </aside>

  <nav class="topnav">
    <span>MENU 1</span><span>MENU 2</span><span>MENU 3</span>
    <span class="dots"><i></i><i></i><i></i></span>
    <span class="avatar" role="img" aria-label="User avatar"></span>
    <span class="user">Theo Marsh</span>
    <svg width="7" height="5" viewBox="0 0 7 5"><path d="M1 1l2.5 2.5L6 1" fill="none" stroke="#2b8d91" stroke-width="1.2"/></svg>
  </nav>

  <h1 class="page-title">Alicante 2017 (Folder Name)</h1>
  <div class="rule"></div>
  <div class="toolbar-label">Thumbnails:</div>
  <div class="view-toggle on" style="left:252px">
    <svg width="9" height="9" viewBox="0 0 9 9" fill="#1f3553"><rect width="4" height="4"/><rect x="5" width="4" height="4"/><rect y="5" width="4" height="4"/><rect x="5" y="5" width="4" height="4"/></svg>
  </div>
  <div class="view-toggle" style="left:267px">
    <svg width="9" height="9" viewBox="0 0 9 9" fill="#c5ccd3"><rect width="2.4" height="2.4"/><rect x="3.3" width="2.4" height="2.4"/><rect x="6.6" width="2.4" height="2.4"/><rect y="3.3" width="2.4" height="2.4"/><rect x="3.3" y="3.3" width="2.4" height="2.4"/><rect x="6.6" y="3.3" width="2.4" height="2.4"/><rect y="6.6" width="2.4" height="2.4"/><rect x="3.3" y="6.6" width="2.4" height="2.4"/><rect x="6.6" y="6.6" width="2.4" height="2.4"/></svg>
  </div>
  <div class="btn-upload">
    <svg width="11" height="8" viewBox="0 0 11 8"><path d="M3 8H2.5A2.5 2.5 0 0 1 2.6 3 3.2 3.2 0 0 1 8.7 2.6 2.7 2.7 0 0 1 8.5 8H8" fill="#fff"/><path d="M5.5 7.5V4M4 5.4l1.5-1.5L7 5.4" stroke="#1f3553" stroke-width="1" fill="none"/></svg>
    UPLOAD
  </div>
  <div class="btn-trash">
    <svg width="8" height="9" viewBox="0 0 8 9"><path d="M1 2h6M3 2V1h2v1M1.8 2.5l.5 5.5h3.4l.5-5.5" fill="none" stroke="#1f3553" stroke-width=".9"/></svg>
  </div>

  <div class="photo selected" style="left:210px;top:109px;background:linear-gradient(160deg,#f3c66b,#e88a2a 60%,#8a4a1e)" role="img" aria-label="Skateboarder jumping at sunset"><span class="tick"><svg width="7" height="6" viewBox="0 0 7 6"><path d="M1 3l1.8 1.8L6 1" stroke="#fff" stroke-width="1.2" fill="none"/></svg></span></div>
  <div class="photo selected" style="left:369px;top:109px;background:linear-gradient(160deg,#c9b9a3,#5b6470 55%,#2d3440)" role="img" aria-label="Friends sitting with a longboard"><span class="tick"><svg width="7" height="6" viewBox="0 0 7 6"><path d="M1 3l1.8 1.8L6 1" stroke="#fff" stroke-width="1.2" fill="none"/></svg></span></div>
  <div class="photo" style="left:529px;top:109px;background:linear-gradient(160deg,#efe4d6,#c99a6a 60%,#7a5a40)" role="img" aria-label="Beagle next to a skateboard"></div>
  <div class="photo" style="left:688px;top:109px;background:linear-gradient(160deg,#6d8a4a,#b24a3a 55%,#3c5a3a)" role="img" aria-label="Friends having a picnic"></div>

  <div class="photo selected" style="left:210px;top:230px;background:linear-gradient(160deg,#5a4038,#2a2226 50%,#e0772a)" role="img" aria-label="Toasting marshmallows over a campfire"><span class="tick"><svg width="7" height="6" viewBox="0 0 7 6"><path d="M1 3l1.8 1.8L6 1" stroke="#fff" stroke-width="1.2" fill="none"/></svg></span></div>
  <div class="photo selected" style="left:369px;top:230px;background:linear-gradient(160deg,#8a7a5e,#5a4a3a 55%,#2a2420)" role="img" aria-label="Friends at a barbecue"><span class="tick"><svg width="7" height="6" viewBox="0 0 7 6"><path d="M1 3l1.8 1.8L6 1" stroke="#fff" stroke-width="1.2" fill="none"/></svg></span></div>
  <div class="photo" style="left:529px;top:230px;background:linear-gradient(160deg,#c8d8a0,#6f9a4a 55%,#3a5a3a)" role="img" aria-label="Friends fishing by a lake"></div>
  <div class="photo" style="left:688px;top:230px;background:linear-gradient(180deg,#e6eef2,#8fc9b4 55%,#7a8a5a)" role="img" aria-label="Mint camper van in a field"></div>

  <div class="photo" style="left:210px;top:350px;background:linear-gradient(160deg,#eadccc,#c9a88a 55%,#8a6a50)" role="img" aria-label="Relaxing with bare feet inside a van"></div>
  <div class="photo" style="left:369px;top:350px;background:linear-gradient(160deg,#cfe2ec,#3aa0c8 50%,#e8b84a)" role="img" aria-label="Surfboards on a beach"></div>
  <div class="photo" style="left:529px;top:350px;background:linear-gradient(180deg,#1f7aa8,#0f4c73)" role="img" aria-label="Surfer seen underwater"></div>
  <div class="photo" style="left:688px;top:350px;background:linear-gradient(180deg,#2f7fb8,#1a5a90 50%,#d8ecf4)" role="img" aria-label="Surfer riding a wave"></div>

  <div class="photo" style="left:210px;top:471px;background:linear-gradient(180deg,#3e86c8,#9fc8e6 60%,#3a6a4a)" role="img" aria-label="Kitesurfer in the air"></div>
  <div class="photo" style="left:369px;top:471px;background:linear-gradient(180deg,#2a6a9a,#1a4a70)" role="img" aria-label="Jet ski on the sea"></div>
  <div class="photo" style="left:529px;top:471px;background:linear-gradient(180deg,#e6c49a,#6a8a9a)" role="img" aria-label="Paddle boarder at sunset"></div>
  <div class="photo" style="left:688px;top:471px;background:linear-gradient(160deg,#f0b08a,#d46a6a 55%,#7a3a4a)" role="img" aria-label="Friends at a festival"></div>

  <div class="photo" style="left:210px;top:592px;background:linear-gradient(180deg,#f2d2a0,#d98a4a 55%,#3a2a2a)" role="img" aria-label="Friends on a beach at sunset"></div>
  <div class="photo" style="left:369px;top:592px;background:linear-gradient(180deg,#2a1e1e,#c8602a)" role="img" aria-label="Bonfire party"></div>
  <div class="photo" style="left:529px;top:592px;background:linear-gradient(180deg,#3a1e1a,#e07a2a)" role="img" aria-label="Bonfire at night"></div>
  <div class="photo" style="left:688px;top:592px;background:linear-gradient(180deg,#cfe0ec,#e6eef2 55%,#8a9aa6)" role="img" aria-label="Runner on a seaside path"></div>

  <div class="photo" style="left:210px;top:714px;background:linear-gradient(160deg,#f6f0e6,#c8c0b4 60%,#6a6a6a)" role="img" aria-label="Skateboarder's feet in bright light"></div>
  <div class="photo" style="left:369px;top:714px;background:linear-gradient(180deg,#bcc0c2,#8a8e90)" role="img" aria-label="Bulldog next to a skateboarder"></div>
  <div class="photo" style="left:529px;top:714px;background:linear-gradient(160deg,#e0dcd8,#8a7a6a 55%,#3a3230)" role="img" aria-label="Man hugging a bulldog"></div>
  <div class="photo" style="left:688px;top:714px;background:linear-gradient(180deg,#5a8ac0,#e6b07a 60%,#5a4a4a)" role="img" aria-label="Cyclist among palm trees at sunset"></div>

  <div class="progress-card" style="left:364px">
    <div class="progress-title">deleting...</div>
    <svg class="ring" width="86" height="86" viewBox="0 0 86 86">
      <circle cx="43" cy="43" r="41" fill="none" stroke="#e9eef0" stroke-width="3"/>
      <circle cx="43" cy="43" r="41" fill="none" stroke="var(--teal)" stroke-width="3" stroke-dasharray="90 168" transform="rotate(-90 43 43)"/>
      <path d="M35 30h16M40 30v-2.5h6V30M36.5 31.5l1.2 14h10.6l1.2-14M41 34.5v8M45 34.5v8" fill="none" stroke="var(--teal)" stroke-width="1.6"/>
    </svg>
    <div class="percent">35%</div>
    <div class="completed">COMPLETED</div>
  </div>
  <div class="progress-card" style="left:540px">
    <div class="progress-title">moving...</div>
    <svg class="ring" width="86" height="86" viewBox="0 0 86 86">
      <circle cx="43" cy="43" r="41" fill="none" stroke="#e9eef0" stroke-width="3"/>
      <circle cx="43" cy="43" r="41" fill="none" stroke="var(--teal)" stroke-width="3" stroke-dasharray="90 168" transform="rotate(-90 43 43)"/>
      <path d="M35 30l7 7-7 7M43 30l7 7-7 7" fill="none" stroke="var(--teal)" stroke-width="2.6" stroke-linecap="round" stroke-linejoin="round"/>
    </svg>
    <div class="percent">35%</div>
    <div class="completed">COMPLETED</div>
  </div>

  <footer class="footer">©2018 Teso Vault.&nbsp; | &nbsp;Contact Us&nbsp; | &nbsp;Privacy Policy</footer>
</section>

<div class="separator-band"></div>

<!-- Compact view -->
<section class="screen screen-compact">
  <aside class="sidebar">
    <div class="brand">Teso Vault</div>
    <div class="btn-create">
      <svg width="9" height="8" viewBox="0 0 9 8"><rect x="0" y="1" width="9" height="7" rx="1" fill="#fff"/><rect x="0" y="0" width="4" height="2" rx="1" fill="#fff"/><path d="M4.5 2.6v4M2.5 4.6h4" stroke="#2b8d91" stroke-width="1.2"/></svg>
      CREATE FOLDER
    </div>
    <ul class="folder-list">
      <li class="folder">Inbox</li>
      <li class="folder">80s party</li>
      <li class="folder sub">A day in Oslo</li>
      <li class="folder sub">Alicante after Chrismias</li>
      <li class="folder">A tour of Svendborg</li>
      <li class="folder active">Alicante 2017</li>
      <li class="folder">Bandarban</li>
      <li class="folder two-line">Birds lightly garnished with monkeys and waterfalls</li>
      <li class="folder">Brazil</li>
      <li class="folder two-line">Days in Denmark - Christmas and new years</li>
    </ul>
  </aside>

  <nav class="topnav">
    <span>MENU 1</span><span>MENU 2</span><span>MENU 3</span>
    <span class="dots"><i></i><i></i><i></i></span>
    <span class="avatar" role="img" aria-label="User avatar"></span>
    <span class="user">Theo Marsh</span>
    <svg width="7" height="5" viewBox="0 0 7 5"><path d="M1 1l2.5 2.5L6 1" fill="none" stroke="#2b8d91" stroke-width="1.2"/></svg>
  </nav>

  <h1 class="page-title">Alicante 2017 (Folder Name)</h1>
  <div class="rule"></div>
  <div class="toolbar-label">Thumbnails:</div>
  <div class="view-toggle" style="left:254px">
    <svg width="9" height="9" viewBox="0 0 9 9" fill="#c5ccd3"><rect width="4" height="4"/><rect x="5" width="4" height="4"/><rect y="5" width="4" height="4"/><rect x="5" y="5" width="4" height="4"/></svg>
  </div>
  <div class="view-toggle on" style="left:272px">
    <svg width="9" height="9" viewBox="0 0 9 9" fill="#2b8d91"><rect width="2.4" height="2.4"/><rect x="3.3" width="2.4" height="2.4"/><rect x="6.6" width="2.4" height="2.4"/><rect y="3.3" width="2.4" height="2.4"/><rect x="3.3" y="3.3" width="2.4" height="2.4"/><rect x="6.6" y="3.3" width="2.4" height="2.4"/><rect y="6.6" width="2.4" height="2.4"/><rect x="3.3" y="6.6" width="2.4" height="2.4"/><rect x="6.6" y="6.6" width="2.4" height="2.4"/></svg>
  </div>
  <div class="btn-upload">
    <svg width="11" height="8" viewBox="0 0 11 8"><path d="M3 8H2.5A2.5 2.5 0 0 1 2.6 3 3.2 3.2 0 0 1 8.7 2.6 2.7 2.7 0 0 1 8.5 8H8" fill="#fff"/><path d="M5.5 7.5V4M4 5.4l1.5-1.5L7 5.4" stroke="#1f3553" stroke-width="1" fill="none"/></svg>
    UPLOAD
  </div>
  <div class="btn-trash">
    <svg width="8" height="9" viewBox="0 0 8 9"><path d="M1 2h6M3 2V1h2v1M1.8 2.5l.5 5.5h3.4l.5-5.5" fill="none" stroke="#1f3553" stroke-width=".9"/></svg>
  </div>

  <div class="photo sm" style="left:210px;top:108px;background:linear-gradient(160deg,#f3c66b,#e88a2a 60%,#8a4a1e)" role="img" aria-label="Skateboarder jumping at sunset"></div>
  <div class="photo sm" style="left:289px;top:108px;background:linear-gradient(160deg,#c9b9a3,#5b6470 55%,#2d3440)" role="img" aria-label="Friends sitting with a longboard"></div>
  <div class="photo sm" style="left:369px;top:108px;background:linear-gradient(160deg,#efe4d6,#c99a6a 60%,#7a5a40)" role="img" aria-label="Beagle next to a skateboard"></div>
  <div class="photo sm" style="left:448px;top:108px;background:linear-gradient(160deg,#6d8a4a,#b24a3a 55%,#3c5a3a)" role="img" aria-label="Friends having a picnic"></div>
  <div class="photo sm" style="left:527px;top:108px;background:linear-gradient(160deg,#5a4038,#2a2226 50%,#e0772a)" role="img" aria-label="Toasting marshmallows over a campfire"></div>
  <div class="photo sm" style="left:607px;top:108px;background:linear-gradient(160deg,#8a7a5e,#5a4a3a 55%,#2a2420)" role="img" aria-label="Friends at a barbecue"></div>
  <div class="photo sm" style="left:686px;top:108px;background:linear-gradient(160deg,#c8d8a0,#6f9a4a 55%,#3a5a3a)" role="img" aria-label="Friends fishing by a lake"></div>
  <div class="photo sm" style="left:766px;top:108px;background:linear-gradient(180deg,#e6eef2,#8fc9b4 55%,#7a8a5a)" role="img" aria-label="Mint camper van in a field"></div>

  <div class="photo sm" style="left:210px;top:169px;background:linear-gradient(160deg,#eadccc,#c9a88a 55%,#8a6a50)" role="img" aria-label="Relaxing with bare feet inside a van"></div>
  <div class="photo sm" style="left:289px;top:169px;background:linear-gradient(160deg,#cfe2ec,#3aa0c8 50%,#e8b84a)" role="img" aria-label="Surfboards on a beach"></div>
  <div class="photo sm" style="left:369px;top:169px;background:linear-gradient(180deg,#1f7aa8,#0f4c73)" role="img" aria-label="Surfer seen underwater"></div>
  <div class="photo sm" style="left:448px;top:169px;background:linear-gradient(180deg,#2f7fb8,#1a5a90 50%,#d8ecf4)" role="img" aria-label="Surfer riding a wave"></div>
  <div class="photo sm" style="left:527px;top:169px;background:linear-gradient(180deg,#3e86c8,#9fc8e6 60%,#3a6a4a)" role="img" aria-label="Kitesurfer in the air"></div>
  <div class="photo sm" style="left:607px;top:169px;background:linear-gradient(180deg,#2a6a9a,#1a4a70)" role="img" aria-label="Jet ski on the sea"></div>
  <div class="photo sm" style="left:686px;top:169px;background:linear-gradient(180deg,#e6c49a,#6a8a9a)" role="img" aria-label="Paddle boarder at sunset"></div>
  <div class="photo sm" style="left:766px;top:169px;background:linear-gradient(160deg,#f0b08a,#d46a6a 55%,#7a3a4a)" role="img" aria-label="Friends at a festival"></div>

  <div class="photo sm" style="left:210px;top:230px;background:linear-gradient(180deg,#f2d2a0,#d98a4a 55%,#3a2a2a)" role="img" aria-label="Friends on a beach at sunset"></div>
  <div class="photo sm" style="left:289px;top:230px;background:linear-gradient(180deg,#6a7a9a,#2a2232)" role="img" aria-label="Party crowd in silhouette"></div>
  <div class="photo sm" style="left:369px;top:230px;background:linear-gradient(180deg,#3a1e1a,#e07a2a)" role="img" aria-label="Bonfire at night"></div>
  <div class="photo sm" style="left:448px;top:230px;background:linear-gradient(180deg,#cfe0ec,#e6eef2 55%,#8a9aa6)" role="img" aria-label="Runner on a seaside path"></div>
  <div class="photo sm" style="left:527px;top:230px;background:linear-gradient(160deg,#f6f0e6,#c8c0b4 60%,#6a6a6a)" role="img" aria-label="Skateboarder's feet in bright light"></div>
  <div class="photo sm" style="left:607px;top:230px;background:linear-gradient(180deg,#bcc0c2,#8a8e90)" role="img" aria-label="Bulldog next to a skateboarder"></div>
  <div class="photo sm" style="left:686px;top:230px;background:linear-gradient(160deg,#e0dcd8,#8a7a6a 55%,#3a3230)" role="img" aria-label="Man hugging a bulldog"></div>
  <div class="photo sm" style="left:766px;top:230px;background:linear-gradient(180deg,#5a8ac0,#e6b07a 60%,#5a4a4a)" role="img" aria-label="Cyclist among palm trees at sunset"></div>
</section>

</body>
</html>
```